High-End Medical Center Website Design Project

This design is part of a well thought-out project by an experienced project manager / developer. The approved wireframe is attached. Creative interpretations / suggestions based on the layout encouraged.

The design is for a new state-of-the-art medical center located in Dallas, Texas. The target audience would likely be individuals (approx. 60% female /40% male) who are the healthcare decision-makers for their families. They would likely have insurance and be inclined to seek out top-quality care.

Potential clients would choose this client over others in their industry because the medical center is physician owned, meaning it is patient-focused rather than profit-focused. The facility is brand new, featuring the latest technology. (This includes an amazing waiting room featuring WiFi and docking stations.) The physicians are hand-picked by referral only.

The look of the site should be extremely clean. We are going for a well-organized, professional look with a bit of a warm glow (interpret that however you like). Use crisp corners and the colors in the logo.

Think modern, clean with some great use of color / font.

We can get lovely photography of the medical center once construction is complete. Feel free to use an "example image" behind the Featured Area ("Physician Owned. Patient-Focused") if you like. We are open to ideas.

ONE CHANGE REQUESTED IN THE WIREFRAME:

Remove the "Connect" 1/4 page footer area and replace with a quick contact form. You may swap the "Locations" area with the form if desired. Put social media icons at the top left of the page in the top header area.

(Note: Please use social media icons that match the design rather than standard icons. We preferred not placing the icons at the top, but the client requested this. Let's not bring more attention to them than necessary.)
Updates

We're custom programming this site, so there's no need to base it on a template. Also, we would prefer not to use typical "seen everywhere" stock images.Thanks.

Industry/Entity Type

Construction

Requirements
Must have
• Follow the wireframe. This has been approved.
Nice to have
• Examples of what hover states, links or dropdowns might look like.

```html
<!DOCTYPE html>
<html lang="en">
<head>
<meta charset="utf-8">
<title>Crest Medical Center</title>
<link href="https://fonts.googleapis.com/css2?family=Arvo:wght@400;700&family=Roboto+Condensed:wght@700&family=Ubuntu:ital,wght@0,400;0,500;1,500&display=swap" rel="stylesheet">
<style>
:root{
  --navy-deep:#08223d;
  --navy:#0b4f97;
  --blue:#0c58a3;
  --blue-band-top:#0a5aa8;
  --blue-band-bottom:#3aa7b7;
  --teal:#3a9aa6;
  --teal-dark:#0e5a66;
  --cyan:#35c4e6;
  --yellow:#f2b200;
  --header-bg:#f4f7fc;
  --page:#ffffff;
  --text:#444b52;
  --heading:#222a33;
  --footer-top:#0b5eae;
  --footer-bottom:#1b93d2;
  --button:#0b57a4;
  --submit:#a6d3ef;
}
*{box-sizing:border-box;margin:0;padding:0}
html,body{width:733px;height:1200px;overflow:hidden;background:var(--page)}
body{font-family:"Ubuntu",Arial,sans-serif;color:var(--text);position:relative}
.abs{position:absolute}

/* top bar */
.top-bar{left:0;top:0;width:733px;height:27px;background:var(--navy-deep)}
.social{top:5px;width:17px;height:17px;border-radius:50%;background:#3f86c9}
.call-now{right:62px;top:6px;font:italic 700 13px/15px Arial,sans-serif;color:#fff;display:flex;align-items:center;gap:6px;letter-spacing:.3px;white-space:nowrap}
.call-now .number{color:var(--cyan)}

/* header */
.site-header{left:0;top:27px;width:733px;height:83px;background:var(--header-bg)}
.brand{left:40px;top:57px;display:flex;align-items:center;gap:8px;white-space:nowrap}
.brand-mark{width:12px;height:12px;background:var(--navy)}
.brand-name{font:700 15px/18px "Arvo",serif;color:var(--navy);letter-spacing:0}
.main-nav{left:308px;top:63px;font:400 10.5px/12px Arial,sans-serif;color:#111;display:flex;gap:7px;white-space:nowrap}
.main-nav a{color:#111;text-decoration:none}
.main-nav a:hover{color:var(--blue)}

/* hero band */
.hero-band{left:0;top:110px;width:733px;height:242px;background:linear-gradient(180deg,var(--blue-band-top) 0%,#0d66ad 55%,var(--blue-band-bottom) 100%)}
.hero-curve{left:0;top:298px;width:733px;height:56px}
.slider{left:40px;top:150px;width:634px;height:267px;border:4px solid #a9adb2;background:#fff;overflow:hidden}
.slider-photo{left:0;top:0;width:430px;height:259px;background:linear-gradient(90deg,#c9d3d8 0%,#dfe7ea 45%,#eef4f6 75%,rgba(255,255,255,0) 100%)}
.slider-title{left:316px;top:104px;font:700 23px/30px "Arvo",serif;color:var(--blue);letter-spacing:.3px;white-space:nowrap}
.slider-title .accent{color:#3d9ea9}
.slider-arrow{top:274px;width:21px;height:21px;background:var(--yellow);color:#222;font:700 13px/21px Arial,sans-serif;text-align:center}

/* features */
.section-title{left:40px;top:429px;width:634px;display:flex;align-items:center;gap:12px}
.section-title .rule{flex:1;height:4px;border-top:1px solid var(--blue);border-bottom:1px solid var(--blue)}
.section-title h2{font:700 21px/26px "Arvo",serif;color:var(--blue);letter-spacing:.5px;white-space:nowrap}
.feature{top:464px;width:193px}
.feature h3{height:17px;background:var(--teal);color:#fff;font:700 11px/17px "Roboto Condensed",Arial,sans-serif;padding-left:4px}
.feature-photo{margin-top:5px;height:92px;border:1px solid #c8ccd0;padding:2px}
.feature-photo div{width:100%;height:100%}
.feature p{margin-top:10px;font-size:8.6px;line-height:11.6px;height:46px}
.feature .divider{margin-top:12px;border-top:1px dashed #9aa0a6}
.btn{display:inline-block;background:var(--button);color:#fff;font:500 8.5px/15px "Ubuntu",Arial,sans-serif;padding:0 6px;text-decoration:none;white-space:nowrap}
.btn::after{content:"";display:inline-block;margin-left:4px;border-left:4px solid #fff;border-top:3px solid transparent;border-bottom:3px solid transparent}
.btn:hover{background:var(--teal)}
.feature .btn{position:absolute;right:0;top:190px}

/* welcome */
.welcome-title{left:40px;top:694px;font:700 17.5px/24px "Arvo",serif;color:var(--heading);letter-spacing:.2px;white-space:nowrap}
.welcome-title span{color:var(--blue)}
.welcome-photo{left:40px;top:724px;width:152px;height:167px;border:1px solid #c8ccd0;padding:3px}
.welcome-photo div{width:100%;height:100%;background:radial-gradient(ellipse at 55% 50%,#ffffff 0%,#e7ecef 55%,#cfd6da 100%)}
.welcome-text{left:200px;top:721px;width:268px;font-size:8.6px;line-height:11.6px}
.welcome-text p{margin-bottom:11.6px}
.welcome-btn{left:200px;top:876px}

/* testimonials */
.testimonials{left:480px;top:700px;width:194px;height:191px;border:1px solid #d3d6da;background:#fff}
.testimonials h2{position:absolute;left:4px;top:4px;width:184px;height:27px;background:var(--teal-dark);color:#fff;font:700 16px/27px "Arvo",serif;text-align:center;letter-spacing:.5px}
.testimonial-photo{left:5px;top:43px;width:60px;height:50px;background:#111;border:1px solid #bbb}
.quote-side{left:79px;top:40px;width:108px;font-size:8.6px;line-height:11.6px}
.quote-full{left:6px;top:101px;width:182px;font-size:8.6px;line-height:11.6px}
.testimonial-rule{left:6px;top:147px;width:182px;border-top:1px dashed #555}
.testimonial-name{left:9px;top:152px;font:italic 500 8.5px/11px "Ubuntu",Arial,sans-serif;color:var(--teal-dark);white-space:nowrap}
.testimonials .btn{position:absolute;right:8px;top:170px}

/* footer */
.site-footer{left:0;top:931px;width:733px;height:269px;background:linear-gradient(180deg,var(--footer-top) 0%,#1482c6 70%,var(--footer-bottom) 100%);color:#fff}
.footer-col{top:23px}
.footer-col h2{font:700 12px/14px "Arvo",serif;letter-spacing:.4px}
.news-list{list-style:none;margin-top:15px}
.news-list li{display:flex;gap:6px;height:30px;font-size:8.4px;line-height:11px}
.news-list svg{flex:none;margin-top:1px}
.more-link{display:block;margin-left:26px;margin-top:-2px;font:italic 500 6.5px/8px "Ubuntu",Arial,sans-serif;color:var(--cyan);text-decoration:none}
.contact-intro{margin-top:13px;width:175px;font-size:8.4px;line-height:11px}
.contact-form input{display:block;width:114px;height:17px;margin-top:6px;border:none;background:#fff;font:400 8px "Ubuntu",Arial,sans-serif;padding-left:5px;color:#666}
.contact-form input:first-child{margin-top:10px}
.contact-form button{display:block;margin-top:7px;width:46px;height:16px;border:none;background:var(--submit);color:#fff;font:500 8px "Ubuntu",Arial,sans-serif;letter-spacing:.3px}
.footer-rule{left:40px;width:634px;border-top:1px solid rgba(255,255,255,.25)}
.footer-note{left:0;width:733px;text-align:center;font:400 7.8px/10px Arial,sans-serif}
</style>
</head>
<body>

<div class="abs top-bar">
  <span class="abs social" style="left:46px"></span>
  <span class="abs social" style="left:69px"></span>
  <span class="abs social" style="left:92px"></span>
  <div class="abs call-now">
    <svg width="26" height="16" viewBox="0 0 26 16" aria-hidden="true">
      <circle cx="13" cy="4" r="3.3" fill="#fff"/><path d="M7 14c0-4 3-6 6-6s6 2 6 6z" fill="#fff"/>
      <circle cx="5" cy="6" r="2.4" fill="#9fd3ef"/><path d="M0.5 14c0-3 2-4.5 4.5-4.5S9.5 11 9.5 14z" fill="#9fd3ef"/>
      <circle cx="21" cy="6" r="2.4" fill="#9fd3ef"/><path d="M16.5 14c0-3 2-4.5 4.5-4.5s4.5 1.5 4.5 4.5z" fill="#9fd3ef"/>
    </svg>
    <span>CALL NOW</span><span class="number">- (555) 014-2290</span>
  </div>
</div>

<header class="abs site-header"></header>
<div class="abs brand"><span class="brand-mark"></span><span class="brand-name">CREST MEDICAL CENTER</span></div>
<nav class="abs main-nav">
  <a href="#">WHY CREST</a><span>|</span><a href="#">PHYSICIANS</a><span>|</span><a href="#">SPECIALITIES</a><span>|</span><a href="#">INFO</a><span>|</span><a href="#">LOCATIONS</a><span>|</span><a href="#">CONTACT</a>
</nav>

<div class="abs hero-band"></div>
<svg class="abs hero-curve" viewBox="0 0 733 56" preserveAspectRatio="none" aria-hidden="true">
  <path d="M0 56V20C10 4 28 2 40 16V56z" fill="#e9f1f7"/>
</svg>
<div class="abs" style="left:0;top:352px;width:733px;height:579px;background:#fff"></div>

<div class="abs slider">
  <div class="abs slider-photo" role="img" aria-label="Photo of a senior physician and a nurse reviewing a tablet"></div>
  <div class="abs slider-title">PHYSICIANS OWNED,<br><span class="accent">PATIENTS FOCUSED</span></div>
</div>
<div class="abs slider-arrow" style="left:33px">&lt;</div>
<div class="abs slider-arrow" style="left:661px">&gt;</div>

<div class="abs section-title"><span class="rule"></span><h2>WHAT SETS US APART</h2><span class="rule"></span></div>

<section class="abs feature" style="left:40px">
  <h3>TECHNOLOGY</h3>
  <div class="feature-photo"><div role="img" aria-label="Photo of imaging equipment and monitors in a scan room" style="background:linear-gradient(90deg,#b8a894,#56646f 45%,#3b4a58 75%,#8a8f93)"></div></div>
  <p>Lorem ipsum dolor sit amet, consectetur adipiscing elit. Quisque dolor eros, consectetur at ante quis, mollis ultrices tortor. Maecenas et risus id nisl vehicula hendrerit a sit amet lorem.</p>
  <div class="divider"></div>
  <a class="btn" href="#">Read More</a>
</section>
<section class="abs feature" style="left:261px">
  <h3>QUALITY OF CORE</h3>
  <div class="feature-photo"><div role="img" aria-label="Photo of a medical team standing around a seated patient" style="background:linear-gradient(90deg,#e9eef0,#8fb6b3 40%,#5fa7a0 60%,#e6ecee)"></div></div>
  <p>Lorem ipsum dolor sit amet, consectetur adipiscing elit. Quisque dolor eros, consectetur at ante quis, mollis ultrices tortor. Maecenas et risus id nisl vehicula hendrerit a sit amet lorem.</p>
  <div class="divider"></div>
  <a class="btn" href="#">Read More</a>
</section>
<section class="abs feature" style="left:482px">
  <h3>PATIENT EXPERIENCE</h3>
  <div class="feature-photo"><div role="img" aria-label="Photo of a doctor talking with an elderly patient in a bright hallway" style="background:linear-gradient(90deg,#9cc3b4,#c9d8d4 40%,#dfe6ea 65%,#b9c2c8)"></div></div>
  <p>Lorem ipsum dolor sit amet, consectetur adipiscing elit. Quisque dolor eros, consectetur at ante quis, mollis ultrices tortor. Maecenas et risus id nisl vehicula hendrerit a sit amet lorem.</p>
  <div class="divider"></div>
  <a class="btn" href="#">Read More</a>
</section>

<h2 class="abs welcome-title">WELCOME TO <span>CREST MEDICAL CENTER</span></h2>
<div class="abs welcome-photo"><div role="img" aria-label="Photo of a teal stethoscope on a white surface"></div></div>
<div class="abs welcome-text">
  <p>Lorem ipsum dolor sit amet, consectetur adipiscing elit. Quisque dolor eros, consectetur at ante quis, mollis ultrices tortor. Maecenas et risus id nisl vehicula hendrerit a sit amet lorem.</p>
  <p>Lorem ipsum dolor sit amet, consectetur adipiscing elit. Quisque dolor eros, consectetur at ante quis, mollis ultrices tortor. Maecenas et risus id nisl vehicula hendrerit a sit amet lorem.</p>
  <p>Lorem ipsum dolor sit amet, consectetur adipiscing elit. Quisque dolor eros, consectetur at ante quis, mollis ultrices tortor. Maecenas et risus id nisl vehicula hendrerit a sit amet lorem. mollis ultrices tortor. Maecenas et risus id nisl vehicula hendrerit a sit amet lorem.</p>
</div>
<a class="abs btn welcome-btn" href="#">Read More</a>

<aside class="abs testimonials">
  <h2>TESTIMONIALS</h2>
  <div class="abs testimonial-photo" role="img" aria-label="Portrait placeholder of the client"></div>
  <p class="abs quote-side">Praesent ultrices, odio iaculis fermentum aliquet, tellus sapien lobortis odio, vitae tempus est neque sed massa.</p>
  <p class="abs quote-full">Nullam vehicula blandit lectus, sit amet lacinia lectus lobortis ac. Aliquam sit amet adipiscing dolor. Etiam porttitor dictum massa.</p>
  <div class="abs testimonial-rule"></div>
  <p class="abs testimonial-name">Mark Ellison, CEO Bluefield Studio</p>
  <a class="btn" href="#">Read More</a>
</aside>

<footer class="abs site-footer">
  <div class="abs footer-col" style="left:48px;width:180px">
    <h2>LATEST NEWS</h2>
    <ul class="news-list">
      <li><svg width="20" height="16" viewBox="0 0 20 16" aria-hidden="true"><path d="M10 1C5 1 1.5 3.8 1.5 7.2c0 2 1.2 3.7 3 4.8L3.5 15l4.2-2.2c.7.1 1.5.2 2.3.2 5 0 8.5-2.8 8.5-6.2S15 1 10 1z" fill="none" stroke="#fff" stroke-width="1.4"/></svg><span>Proin sit amet ipsum sagittis, aliquam mauris sed, laoreet arcu.</span></li>
      <li><svg width="20" height="16" viewBox="0 0 20 16" aria-hidden="true"><path d="M10 1C5 1 1.5 3.8 1.5 7.2c0 2 1.2 3.7 3 4.8L3.5 15l4.2-2.2c.7.1 1.5.2 2.3.2 5 0 8.5-2.8 8.5-6.2S15 1 10 1z" fill="none" stroke="#fff" stroke-width="1.4"/></svg><span>Nullam sollicitudin risus in urna pulvinar lacinia in quis arcu.</span></li>
      <li><svg width="20" height="16" viewBox="0 0 20 16" aria-hidden="true"><path d="M10 1C5 1 1.5 3.8 1.5 7.2c0 2 1.2 3.7 3 4.8L3.5 15l4.2-2.2c.7.1 1.5.2 2.3.2 5 0 8.5-2.8 8.5-6.2S15 1 10 1z" fill="none" stroke="#fff" stroke-width="1.4"/></svg><span>Aliquam scelerisque lorem at elit scelerisque interdum.</span></li>
      <li><svg width="20" height="16" viewBox="0 0 20 16" aria-hidden="true"><path d="M10 1C5 1 1.5 3.8 1.5 7.2c0 2 1.2 3.7 3 4.8L3.5 15l4.2-2.2c.7.1 1.5.2 2.3.2 5 0 8.5-2.8 8.5-6.2S15 1 10 1z" fill="none" stroke="#fff" stroke-width="1.4"/></svg><span>Curabitur vel tellus vitae enim commodo dictum a eget magna.</span></li>
    </ul>
    <a class="more-link" href="#">Read More</a>
  </div>
  <div class="abs footer-col" style="left:276px;width:180px">
    <h2>LATEST BLOG</h2>
    <ul class="news-list">
      <li><svg width="20" height="16" viewBox="0 0 20 16" aria-hidden="true"><path d="M10 1C5 1 1.5 3.8 1.5 7.2c0 2 1.2 3.7 3 4.8L3.5 15l4.2-2.2c.7.1 1.5.2 2.3.2 5 0 8.5-2.8 8.5-6.2S15 1 10 1z" fill="none" stroke="#fff" stroke-width="1.4"/></svg><span>Proin sit amet ipsum sagittis, aliquam mauris sed, laoreet arcu.</span></li>
      <li><svg width="20" height="16" viewBox="0 0 20 16" aria-hidden="true"><path d="M10 1C5 1 1.5 3.8 1.5 7.2c0 2 1.2 3.7 3 4.8L3.5 15l4.2-2.2c.7.1 1.5.2 2.3.2 5 0 8.5-2.8 8.5-6.2S15 1 10 1z" fill="none" stroke="#fff" stroke-width="1.4"/></svg><span>Nullam sollicitudin risus in urna pulvinar lacinia in quis arcu.</span></li>
      <li><svg width="20" height="16" viewBox="0 0 20 16" aria-hidden="true"><path d="M10 1C5 1 1.5 3.8 1.5 7.2c0 2 1.2 3.7 3 4.8L3.5 15l4.2-2.2c.7.1 1.5.2 2.3.2 5 0 8.5-2.8 8.5-6.2S15 1 10 1z" fill="none" stroke="#fff" stroke-width="1.4"/></svg><span>Aliquam scelerisque lorem at elit scelerisque interdum.</span></li>
      <li><svg width="20" height="16" viewBox="0 0 20 16" aria-hidden="true"><path d="M10 1C5 1 1.5 3.8 1.5 7.2c0 2 1.2 3.7 3 4.8L3.5 15l4.2-2.2c.7.1 1.5.2 2.3.2 5 0 8.5-2.8 8.5-6.2S15 1 10 1z" fill="none" stroke="#fff" stroke-width="1.4"/></svg><span>Curabitur vel tellus vitae enim commodo dictum a eget magna.</span></li>
    </ul>
    <a class="more-link" href="#">Read More</a>
  </div>
  <div class="abs footer-col" style="left:503px;width:190px">
    <h2>CONTACT US</h2>
    <p class="contact-intro">Just fill in the forms and send, one if our executive will contact with you within one busuness day.</p>
    <form class="contact-form">
      <input type="text" placeholder="Your Name">
      <input type="text" placeholder="Your Mobile No">
      <input type="text" placeholder="Your email id">
      <button type="button">SUBMIT</button>
    </form>
  </div>
  <div class="abs footer-rule" style="top:210px"></div>
  <p class="abs footer-note" style="top:217px">Call or write so we can send a team to your company / mission to discuss our strategy in a relaxed and nonobligatory manner</p>
  <div class="abs footer-rule" style="top:232px"></div>
  <p class="abs footer-note" style="top:239px">© 2013, All Rights Reserved, Crest Care</p>
</footer>

</body>
</html>
```